The Nine Lanterns CD cover and booklet - meditation walks

I have created a CD of five meditation walks for the modern mystic - with a professional voice over and really cool music - to help people find their way back home to their true Self. It is very powerful and life-enhancing. The walks were created on the Canary Island of Lanzarote in Bartolo's garden and I have stunning photographs taken by pro-photographer Owen Fairbrook to accompany the sleeve notes. The result will be a truly beautiful 12pp CD sleeve note booklet - which will itself be so cleanly laid out people will want to pick it up and play! :-) You can do that for me ... and, of course, you will get a free signed copy of the finished CD ... Rudy - The Nine Lanterns - see http://www.thewellspring-example.com/
I will send a CD page layout template, the full text and hi-res images to the selected design partner. I attach sample text docs and lo-res logo.
Extra guaranteed money and extended deadline with helpful files.
Hi there - I'm very excited about what designs I get for The Nine Lanterns CD. Everything is ready to go!
Rudy
Today I have uploaded a hi-res version of The Nine Lanterns logo which you may find helpful.
Rudy
Several designers have requested hi-res images of the pictures on the PDF sample pages - so I have uploaded this evening some additional hi-res images as well as a hi-res logo.
hi all you lovely designers! Today is the last day for submission of designs - so if you want a shout ... its now or never. :-)

```html
<!DOCTYPE html>
<html lang="en">
<head>
<meta charset="utf-8">
<title>The Nine Lanterns – CD label, tray card and booklet</title>
<link href="https://fonts.googleapis.com/css2?family=Delius&family=Fredoka:wght@600&display=swap" rel="stylesheet">
<style>
  :root {
    --paper: #ffffff;
    --ink: #1f1f1f;
    --title-orange: #f15a22;
    --title-outline: #3a1a0a;
    --spine-tan: #c9a98b;
    --panel-white: rgba(255, 255, 255, 0.78);
    --frame: #111111;
    --sky-top: #8fa3b4;
    --sky-low: #c9d1d4;
    --sea: #3f8f93;
    --sand: #d9c4a0;
    --sand-deep: #c9ae86;
    --cave-dark: #1a2622;
    --cave-green: #5f7f3a;
    --cave-light: #e9efdf;
    --water: #0f2630;
    --succulent-green: #9bb45a;
    --succulent-pink: #d98c6a;
    --body-font: "Delius", "Comic Sans MS", cursive;
    --title-font: "Fredoka", "Arial Rounded MT Bold", sans-serif;
  }
  * { box-sizing: border-box; margin: 0; padding: 0; }
  html, body { width: 1200px; height: 1000px; overflow: hidden; background: var(--paper); }
  .canvas { position: relative; width: 1200px; height: 1000px; font-family: var(--body-font); color: var(--ink); }

  .photo-fill { position: absolute; inset: 0; }
  .beach-fill {
    background: linear-gradient(var(--sky-top) 0%, var(--sky-low) 34%, var(--sea) 40%, #a9c6c0 45%, var(--sand) 50%, var(--sand-deep) 100%);
  }

  .brand-title {
    font-family: var(--title-font);
    font-weight: 600;
    color: var(--title-orange);
    -webkit-text-stroke: 1px var(--title-outline);
    line-height: 1;
  }
  .publisher-mark {
    position: absolute;
    display: flex; align-items: center; gap: 6px;
    font-family: var(--body-font);
    font-size: 14px;
    color: var(--ink);
  }
  .publisher-mark .dot { width: 14px; height: 14px; border-radius: 50%; background: var(--title-orange); flex: none; }

  /* CD label */
  .disc { position: absolute; left: 61px; top: 42px; width: 456px; height: 456px; border-radius: 50%; overflow: hidden; }
  .disc-hole { position: absolute; left: 204px; top: 204px; width: 48px; height: 48px; border-radius: 50%; background: var(--paper); }
  .disc-title { position: absolute; left: 140px; top: 40px; font-size: 30px; }
  .disc-subtitle { position: absolute; left: 145px; top: 114px; font-size: 16px; line-height: 1.05; color: #1b2a3a; }
  .disc-credit { position: absolute; left: 325px; top: 153px; font-size: 12px; line-height: 1.1; text-align: center; }
  .disc .publisher-mark { left: 318px; top: 200px; }

  /* Tray card */
  .tray { position: absolute; left: 644px; top: 46px; width: 506px; height: 452px; }
  .cave-fill {
    background: radial-gradient(ellipse at 50% 14%, var(--cave-light) 0 10%, var(--cave-green) 22%, transparent 45%),
                linear-gradient(var(--cave-dark) 0 48%, var(--water) 100%);
  }
  .frame-line { position: absolute; inset: 6px; border: 1px solid var(--frame); pointer-events: none; }
  .track-panel { position: absolute; left: 159px; top: 157px; width: 263px; height: 177px;
    background: var(--panel-white); border-radius: 22px; padding: 22px 24px 0 32px; }
  .track-panel .brand-title { font-size: 25px; margin-bottom: 10px; }
  .track-list { list-style: none; font-size: 12.5px; line-height: 16.5px; color: #3a3f45; }
  .track-list li { display: flex; justify-content: space-between; }

  /* Booklet front */
  .booklet-front { position: absolute; left: 86px; top: 521px; width: 506px; height: 452px; }
  .booklet-front .frame-line { inset: 11px; }
  .booklet-front .publisher-mark { left: 28px; top: 45px; }
  .front-kicker { position: absolute; left: 134px; top: 32px; font-size: 21px; letter-spacing: 0.5px; }
  .front-about { position: absolute; left: 216px; top: 72px; display: flex; align-items: baseline; gap: 6px; }
  .front-about span:first-child { font-size: 15px; }
  .front-about .brand-title { font-size: 25px; }
  .via-list { position: absolute; left: 272px; top: 112px; list-style: none; font-size: 15px; line-height: 19px; color: #1b2130; }

  /* Spine */
  .spine { position: absolute; left: 592px; top: 521px; width: 72px; height: 452px; background: var(--spine-tan); }
  .spine .frame-line { inset: 11px 9px; }
  .spine-text { position: absolute; left: 18px; top: 30px; height: 340px;
    writing-mode: vertical-rl; transform: rotate(180deg); white-space: nowrap; }
  .spine-text .brand-title { display: block; font-size: 19px; line-height: 20px; }
  .spine-text .spine-sub { display: block; font-size: 13px; line-height: 18px; }

  /* Booklet back */
  .booklet-back { position: absolute; left: 664px; top: 521px; width: 486px; height: 452px; }
  .garden-fill {
    background: radial-gradient(circle at 10% 15%, var(--succulent-pink) 0 14%, transparent 26%),
                radial-gradient(circle at 88% 12%, #3c3a38 0 15%, transparent 28%),
                linear-gradient(135deg, #6f8e3a, var(--succulent-green) 45%, #7aa06a 80%, #4a6b58);
  }
  .booklet-back .frame-line { inset: 11px; }
  .notes-panel { position: absolute; left: 26px; top: 115px; width: 415px; height: 280px;
    background: var(--panel-white); border-radius: 26px; padding: 20px 20px 0 18px; font-size: 15px; line-height: 15.5px; color: #222; }
  .quote { font-weight: 700; font-size: 15px; }
  .quote-credit { text-align: right; padding-right: 24px; margin-bottom: 14px; }
  .notes-panel p { margin-bottom: 14px; }
  .imprint { font-weight: 700; }
</style>
</head>
<body>
<main class="canvas">

  <!-- CD label -->
  <section class="disc">
    <div class="photo-fill beach-fill" role="img" aria-label="Photo of a stacked lava stone cairn on a smooth dark boulder on a sandy beach by the sea"></div>
    <div class="brand-title disc-title">the<br>Nine Lanterns</div>
    <div class="disc-subtitle">walking meditations<br>for the mystic in you</div>
    <div class="disc-credit">created by<br>Rudy Merriweather</div>
    <div class="publisher-mark"><span class="dot"></span>Solara Publishing</div>
    <div class="disc-hole"></div>
  </section>

  <!-- Tray card -->
  <section class="tray">
    <div class="photo-fill cave-fill" role="img" aria-label="Photo of a lava cave opening onto a garden, reflected in a still dark pool"></div>
    <div class="frame-line"></div>
    <div class="track-panel">
      <div class="brand-title">the Nine Lanterns</div>
      <ol class="track-list">
        <li><span>1. Introduction</span><span>3:52</span></li>
        <li><span>2. Via Positiva</span><span>9:04</span></li>
        <li><span>3. Via Negativa</span><span>6:54</span></li>
        <li><span>4. Via Creativa</span><span>6:22</span></li>
        <li><span>4. Via Transformativa</span><span>5:52</span></li>
        <li><span>5. Via Integrativa</span><span>4:53</span></li>
      </ol>
    </div>
  </section>

  <!-- Booklet front -->
  <section class="booklet-front">
    <div class="photo-fill beach-fill" role="img" aria-label="Photo of a lava stone cairn on a dark boulder on the beach"></div>
    <div class="frame-line"></div>
    <div class="publisher-mark"><span class="dot"></span>Solara</div>
    <div class="front-kicker">the way of the mystic</div>
    <div class="front-about"><span>about</span><span class="brand-title">the Nine Lanterns</span></div>
    <ul class="via-list">
      <li>Via Positiva</li>
      <li>Via Negativa</li>
      <li>Via Creativa</li>
      <li>Via Transformativa</li>
      <li>Via Integrativa</li>
    </ul>
  </section>

  <!-- Spine -->
  <section class="spine">
    <div class="frame-line"></div>
    <div class="spine-text">
      <span class="brand-title">the Nine Lanterns</span>
      <span class="spine-sub">walking meditations for the mystic in you</span>
    </div>
  </section>

  <!-- Booklet back -->
  <section class="booklet-back">
    <div class="photo-fill garden-fill" role="img" aria-label="Photo of pink and green succulents beside dark lava rock"></div>
    <div class="frame-line"></div>
    <div class="notes-panel">
      <div class="quote">“What you are looking for is what is looking.”</div>
      <div class="quote-credit">- Brother Anselm of Tavira</div>
      <p>These walking meditations created in Bartolo’s garden, Lanzarote will make you feel grounded and uplifted, centred and expansive, connected with your deepest purpose and your true Self.</p>
      <p class="imprint">Solara Publishing<br>© Solara Publishing 2013<br>www.theninelanterns-example.com</p>
      <p>photo:<br>Playa de las Conchas, La Graciosa, Lanzarote, Canary Islands by Owen Fairbrook, gr8.</p>
    </div>
  </section>

</main>
</body>
</html>
```